The maple crew

I want it as prefession and attractive as possible we are a lawnmowing business

Phone number 605-318-2264
Name- Carlos Whitfield
Email- themaplecrewsd@fernpost.com

```html
<!DOCTYPE html>
<html lang="en">
<head>
<meta charset="UTF-8">
<title>The maple crew — Business Card</title>
<link rel="stylesheet" href="https://fonts.googleapis.com/css2?family=Montserrat:wght@400;500;600;800&display=swap">
<style>
  :root {
    --backdrop: #3a3a3c;
    --forest: #0f4a1e;
    --leaf: #5cbf3f;
    --paper: #ffffff;
    --divider: rgba(255,255,255,0.35);
  }
  * { box-sizing: border-box; margin: 0; padding: 0; }
  html, body { width: 1200px; height: 1200px; overflow: hidden; }
  body {
    background: var(--backdrop);
    font-family: "Montserrat", sans-serif;
    position: relative;
  }
  .card {
    position: absolute;
    left: 170px;
    width: 860px;
    height: 491px;
    border-radius: 34px;
    overflow: hidden;
    box-shadow: 0 14px 30px rgba(0,0,0,0.45);
    border-bottom: 6px solid var(--leaf);
  }
  .card--front { top: 70px; background: var(--forest); }
  .card--back { top: 640px; background: var(--forest); }

  .front__top {
    position: absolute;
    left: 0; top: 0; right: 0;
    height: 270px;
    background: var(--paper);
    display: flex;
    align-items: center;
    justify-content: center;
  }
  .front__stripe {
    position: absolute;
    left: 0; right: 0; top: 270px;
    height: 8px;
    background: var(--leaf);
  }
  .front__stripe-gap {
    position: absolute;
    left: 0; right: 0; top: 278px;
    height: 8px;
    background: var(--paper);
  }

  .wordmark {
    display: flex;
    align-items: center;
    gap: 16px;
    font-weight: 800;
    font-size: 46px;
    letter-spacing: 1px;
    text-transform: uppercase;
  }
  .wordmark__square {
    width: 30px; height: 30px;
    background: currentColor;
  }
  .wordmark--light { color: var(--forest); }
  .wordmark--dark { color: var(--paper); font-size: 58px; }

  .front__person {
    position: absolute;
    left: 60px;
    bottom: 60px;
  }
  .person__name {
    color: var(--leaf);
    font-weight: 600;
    font-size: 36px;
    letter-spacing: 0.5px;
    text-transform: uppercase;
  }
  .person__role {
    color: var(--paper);
    font-weight: 500;
    font-size: 24px;
    letter-spacing: 1px;
    margin-top: 2px;
  }
  .front__divider {
    position: absolute;
    left: 480px;
    top: 320px;
    width: 1px;
    height: 110px;
    background: var(--divider);
  }
  .front__contact {
    position: absolute;
    left: 510px;
    top: 320px;
    list-style: none;
    color: var(--paper);
    font-size: 19px;
    font-weight: 400;
  }
  .contact__item {
    display: flex;
    align-items: center;
    gap: 10px;
    margin-bottom: 14px;
  }
  .contact__item svg { width: 22px; height: 22px; fill: var(--leaf); flex: none; }

  .card--back .back__center {
    position: absolute;
    inset: 0;
    display: flex;
    align-items: center;
    justify-content: center;
  }
</style>
</head>
<body>
  <article class="card card--front">
    <div class="front__top">
      <div class="wordmark wordmark--light">
        <span class="wordmark__square"></span>
        <span>The maple crew</span>
      </div>
    </div>
    <div class="front__stripe"></div>
    <div class="front__stripe-gap"></div>

    <div class="front__person">
      <p class="person__name">Carlos Whitfield</p>
      <p class="person__role">OWNER</p>
    </div>

    <div class="front__divider"></div>

    <ul class="front__contact">
      <li class="contact__item">
        <svg viewBox="0 0 24 24" aria-hidden="true"><path d="M6.6 10.8a15.1 15.1 0 0 0 6.6 6.6l2.2-2.2c.3-.3.7-.4 1-.2 1.1.4 2.3.6 3.6.6.6 0 1 .4 1 1V20c0 .6-.4 1-1 1A17 17 0 0 1 3 4c0-.6.4-1 1-1h3.5c.6 0 1 .4 1 1 0 1.3.2 2.5.6 3.6.1.3 0 .7-.2 1z"/></svg>
        <span>605-318-2264</span>
      </li>
      <li class="contact__item">
        <svg viewBox="0 0 24 24" aria-hidden="true"><path d="M2 5h20v14H2zm2 2v.5l8 5 8-5V7zm0 2.8V17h16V9.8l-8 5z"/></svg>
        <span>themaplecrewsd@fernpost.com</span>
      </li>
    </ul>
  </article>

  <article class="card card--back">
    <div class="back__center">
      <div class="wordmark wordmark--dark">
        <span class="wordmark__square"></span>
        <span>The maple crew</span>
      </div>
    </div>
  </article>
</body>
</html>
```